Accountancy Firm A5 flyer Design

We are looking for an eye catching A5 flyer for our firm, it will be sent to SME's therefore it has to look clean, attractive & elegant.

The target audience: SME's, Taxpayers, Companies, Businesses

Highlight this: Specialist Contractor Accountants
Color scheme: Similar to the logo & Website ( www.finvelo.co.uk)
Slogan: Meets your business needs beyond numbers.
Size: A5
Info to be displayed: Logo, Services, why us, Institue logo, Partners logo,
QR code if possible ( small)
Testimonials: https://lnk.example-short.net/Qw7rTz

References: See attached.

https://www.pagemoldix.com/Templates/Flyer/Financial-Services/Accounting-Bookkeeping/Template-Design-Library.aspx
https://www.pagemoldix.com/Templates/Flyer-Ad/Tax-Preparer-Flyer-Ad-Template-Design-KV5829304.aspx

Target Market(s)

SME's, Taxpayers, Companies, Businesses

Industry/Entity Type

Accounting

Font styles to use
Sans Serif

Colors
ffffff
ec1f27

Requirements
Must have
• eye catching, Highlight this: Specialist Contractor Accountants
• Color scheme: Similar to the logo & Website ( www.finvelo.co.uk)
• Slogan: Meets your business needs beyond numbers.
• Size: A5
• Info to be displayed: Logo, Services, why us, Institue logo, Partners logo,
• QR code if possible ( small)
Nice to have
• Testimonials: https://lnk.example-short.net/Qw7rTz
Should not have
• Bad Color Scheme

```html
<!DOCTYPE html>
<html lang="en">
<head>
<meta charset="utf-8">
<title>Finvelo – Specialist Contractor Accountants</title>
<link href="https://fonts.googleapis.com/css2?family=Oswald:wght@600;700&family=PT+Sans:ital,wght@0,400;0,700;1,400&family=Fira+Sans+Condensed:ital,wght@1,700&display=swap" rel="stylesheet">
<style>
:root{
  --red:#d2302c;
  --ink:#231f20;
  --bar:#4a4444;
  --white:#ffffff;
  --cta-bg:#e6e6e8;
  --text-dark:#1c1c1c;
  --badge-line:#cfcfcf;
  --badge-shape:#c4c4c4;
}
*{margin:0;padding:0;box-sizing:border-box}
html,body{width:901px;height:1200px;overflow:hidden;background:var(--white)}
.flyer{position:relative;width:901px;height:1200px;overflow:hidden;font-family:"PT Sans",sans-serif;background:var(--ink)}
.header{position:absolute;left:0;top:0;width:901px;height:173px;background:var(--red)}
.header h1{position:absolute;left:65px;top:30px;font-family:"Oswald",sans-serif;font-weight:700;font-size:60px;line-height:64px;color:var(--white);letter-spacing:.5px;text-transform:uppercase}
.hero{position:absolute;left:0;top:173px;width:901px;height:502px;
  background:linear-gradient(160deg,#ffffff 0%,#f4f4f4 30%,#dcd8d4 55%,#b9b4ae 75%,#e8e6e4 100%)}
.brand{position:absolute;left:62px;top:200px;display:flex;align-items:center;gap:12px}
.brand-mark{width:40px;height:40px;background:var(--red)}
.brand-name{font-family:"PT Sans",sans-serif;font-weight:700;font-size:52px;color:var(--ink);letter-spacing:2px}
.contact{position:absolute;right:60px;top:193px;text-align:right;color:var(--text-dark);font-size:19px;line-height:27px}
.contact .address{font-weight:700;margin-bottom:12px}
.contact b{font-weight:700}
.slogan-box{position:absolute;left:557px;top:535px;width:304px;height:140px;background:var(--red);color:var(--white);text-align:right;padding:12px 22px 0 0}
.slogan-box .slogan{font-family:"Fira Sans Condensed",sans-serif;font-style:italic;font-weight:700;font-size:26px;line-height:35px}
.slogan-box .web{font-size:25px;font-weight:700;letter-spacing:1.5px;margin-top:20px}
.section-bar{position:absolute;left:0;top:675px;width:901px;height:37px;background:var(--bar);color:var(--white);font-size:23px;font-weight:700}
.section-bar span{position:absolute;top:3px}
.list{position:absolute;list-style:none;color:var(--white);font-size:17px}
.list li{position:relative;padding-left:22px}
.list li::before{content:"";position:absolute;left:0;top:7px;width:10px;height:10px;border-radius:50%;background:var(--red)}
.services{left:48px;top:723px}
.services li{height:24.6px}
.why{left:357px;top:721px}
.why li{height:26.3px}
.badges{position:absolute;left:735px;top:755px;width:124px}
.badge{width:124px;height:52px;background:var(--white);border-radius:3px;margin-bottom:6px;border:1px solid var(--badge-line);display:flex;align-items:center;justify-content:center}
.badge .shape{width:80px;height:14px;background:var(--badge-shape)}
.footer-band{position:absolute;left:0;top:1120px;width:901px;height:80px;background:var(--red)}
.footnote{position:absolute;left:40px;top:1128px;color:var(--white);font-style:italic;font-size:15px;line-height:20px}
.cta{position:absolute;left:358px;top:1049px;width:543px;height:119px;background:var(--cta-bg);text-align:right;padding:6px 40px 0 0;color:var(--bar)}
.cta .cta-line{font-family:"Fira Sans Condensed",sans-serif;font-style:italic;font-weight:700;font-size:34px;line-height:42px}
.cta .cta-phone{font-family:"Oswald",sans-serif;font-weight:600;font-size:46px;line-height:58px;letter-spacing:1px}
</style>
</head>
<body>
<div class="flyer">
  <header class="header">
    <h1>Specialist Contractor<br>Accountants</h1>
  </header>

  <div class="hero" role="img" aria-label="Photo of hands using a calculator and pen beside a laptop and financial chart papers"></div>

  <div class="brand">
    <div class="brand-mark"></div>
    <div class="brand-name">FINVELO</div>
  </div>

  <div class="contact">
    <div class="address">48 Kestrel Lane, Ashwick, AW3 7TN</div>
    <div><b>T :</b> 0203 5562 907, <b>T:</b> 0800 731 4406</div>
    <div><b>E :</b> hello@finvelo.co.uk</div>
  </div>

  <div class="slogan-box">
    <div class="slogan">Meets your business<br>needs beyond numbers</div>
    <div class="web">www.finvelo.co.uk</div>
  </div>

  <div class="section-bar">
    <span style="left:40px">OUR SERVICES:</span>
    <span style="left:357px">Why Us</span>
  </div>

  <ul class="list services">
    <li>Company Formation</li>
    <li>Business Start-up Advice</li>
    <li>Company Accounts</li>
    <li>Company Tax Returns</li>
    <li>Non Resident Landlord Taxes</li>
    <li>Personal Tax Returns</li>
    <li>Landlords Tax Returns</li>
    <li>C.I.S - Tax Refunds</li>
    <li>Tax Investigations</li>
    <li>Tax Planning</li>
    <li>Payroll &amp; PAYE</li>
    <li>Work Place Pension</li>
    <li>Bookkeeping</li>
    <li>Registered Office Address</li>
  </ul>

  <ul class="list why">
    <li>Qualified &amp; experienced team</li>
    <li>Fixed Fees – No surprise bills</li>
    <li>Over 40 years of combined experience</li>
    <li>Dedicated accounts manage</li>
    <li>Monthly Newsletters &amp; tax tips</li>
    <li>Work on time, Every Time</li>
    <li>Free telephone &amp; email support</li>
    <li>Guaranteed&nbsp; Satisfaction</li>
    <li>Never miss any deadline*</li>
    <li>Excellent Customer Service</li>
  </ul>

  <div class="badges" role="img" aria-label="Institute and partner badges">
    <div class="badge"><div class="shape"></div></div>
    <div class="badge"><div class="shape"></div></div>
    <div class="badge"><div class="shape"></div></div>
    <div class="badge"><div class="shape"></div></div>
  </div>

  <div class="footer-band"></div>
  <p class="footnote">*As long as you allow us 28 days for<br>year end accounts &amp; tax returns</p>

  <div class="cta">
    <div class="cta-line">Call us now for FREE Consultation</div>
    <div class="cta-phone">0203 5562 907</div>
  </div>
</div>
</body>
</html>
```